Website and business logo needed

Organisation for the community providing dispute resolution services, peace building.

I'd like calm colours, a strong simple logo symbolising collaboration, peace and cohesion. Needs to convey that message in a symbol.

We provide different types of services so we do mediation, and training and provide publications and research. It's community based and designed to work with the community for the community.

Industry/Entity Type

Training

Contact Information for Business Card

Quiet Harbour - Institute for Neighbourhood and Conflict Settlement
communication skills, mediation, facilitation, conflict coaching, education, training, research
PO Box 7416
South Brisbane
0418 627 903

Requirements
Must have
• Logo
Calm but strong colours

```html
<!DOCTYPE html>
<html lang="en">
<head>
<meta charset="utf-8">
<title>Quiet Harbour – Business Card</title>
<link href="https://fonts.googleapis.com/css2?family=Open+Sans:wght@400;600;700&display=swap" rel="stylesheet">
<style>
  :root {
    --page-bg: #e9e7e3;
    --card-white: #f4f4f4;
    --card-band: #c9c9c9;
    --ink: #3b3b3b;
    --brand-blue: #1c3f8f;
    --blue-deep: #0b1f66;
    --blue-mid: #163a9a;
    --blue-light: #2f7ed8;
    --white: #ffffff;
  }
  * { box-sizing: border-box; margin: 0; padding: 0; }
  html, body {
    width: 1200px; height: 900px; overflow: hidden;
    background: var(--page-bg);
    font-family: "Open Sans", Arial, sans-serif;
  }
  .canvas {
    width: 1200px; height: 900px;
    display: flex; flex-direction: column;
    align-items: center; justify-content: center; gap: 56px;
  }
  .card {
    width: 640px; height: 366px;
    position: relative; overflow: hidden;
    box-shadow: 0 6px 18px rgba(0,0,0,0.18);
  }

  /* Front */
  .card-front { background: var(--card-white); }
  .card-front .identity {
    position: absolute; left: 0; top: 0; right: 0; height: 212px;
    display: flex; align-items: center; padding: 0 36px 0 40px;
  }
  .brand-lockup {
    display: flex; flex-direction: column; align-items: center; gap: 10px;
    width: 170px;
  }
  .brand-dot {
    width: 64px; height: 64px; border-radius: 50%;
    background: var(--brand-blue);
  }
  .brand-name {
    color: var(--brand-blue); font-weight: 700;
    font-size: 22px; line-height: 1.02; text-align: center;
    text-transform: uppercase; letter-spacing: 0.5px;
  }
  .divider {
    width: 2px; height: 120px; background: var(--ink);
    margin: 0 18px 0 18px;
  }
  .services { color: var(--ink); }
  .services .org {
    font-weight: 600; font-size: 14.5px; line-height: 1.3; margin-bottom: 4px;
  }
  .services .list { font-size: 14.5px; line-height: 1.4; }
  .card-front .contact-band {
    position: absolute; left: 0; right: 0; bottom: 0; height: 154px;
    background: var(--card-band);
    display: flex; align-items: center; padding-left: 118px;
    color: var(--ink); font-size: 17px;
  }

  /* Back */
  .card-back {
    background: radial-gradient(ellipse at 65% 40%, var(--blue-light) 0%, var(--blue-mid) 38%, var(--blue-deep) 100%);
    display: flex; flex-direction: column; align-items: center; justify-content: center; gap: 14px;
  }
  .card-back .brand-dot {
    width: 84px; height: 84px; background: var(--white);
  }
  .card-back .brand-name {
    color: var(--white); font-size: 30px;
  }
</style>
</head>
<body>
  <main class="canvas">
    <section class="card card-front" aria-label="Business card front">
      <div class="identity">
        <div class="brand-lockup">
          <span class="brand-dot"></span>
          <span class="brand-name">Quiet<br>Harbour</span>
        </div>
        <span class="divider"></span>
        <div class="services">
          <p class="org">Institute for Neighbourhood and Conflict Settlement</p>
          <p class="list">communication skills | mediation | facilitation<br>conflict coaching | education | training | research</p>
        </div>
      </div>
      <div class="contact-band">
        <p>PO Box 7416 South Brisbane&nbsp; | 0418 627 903</p>
      </div>
    </section>

    <section class="card card-back" aria-label="Business card back">
      <span class="brand-dot"></span>
      <span class="brand-name">Quiet<br>Harbour</span>
    </section>
  </main>
</body>
</html>
```